Natural Spring Water Label Design

We need to have a label design for our natural spring water. We are looking at a transparent label, not necessarily completely transparent but see through with a maximum of 4 colors. For example, the background could be a light blue. Our bottle is a high end bottle so we are looking for the label to reflect this.

i have attached the label we have so far. Same logo and information can be used on the new label. We only want a new look with less colors. I have also attached two labels in the style that we like.

Reason: I am not satisfied with any designs yet.

Requirements
Must have
• Transparent label
Should not have
• no more than 4 colors

```html
<!DOCTYPE html>
<html lang="en">
<head>
<meta charset="utf-8">
<title>Clear Fall Natural Spring Water Label</title>
<link rel="stylesheet" href="https://fonts.googleapis.com/css2?family=Open+Sans:ital,wght@0,300;0,600;0,700;1,600&display=swap">
<style>
  :root {
    --backdrop: #e8e7e4;
    --label-blue: #7488dc;
    --label-edge: #ffffff;
    --ink-white: #ffffff;
  }
  * { box-sizing: border-box; margin: 0; padding: 0; }
  html, body {
    width: 822px;
    height: 1200px;
    overflow: hidden;
    background: var(--backdrop);
  }
  .canvas {
    position: relative;
    width: 822px;
    height: 1200px;
    display: flex;
    align-items: center;
    justify-content: center;
  }
  .label {
    position: relative;
    width: 740px;
    height: 380px;
    background: var(--label-blue);
    opacity: 0.92;
    font-family: "Open Sans", sans-serif;
    color: var(--ink-white);
    text-align: center;
  }
  .label__frame {
    position: absolute;
    inset: 10px;
    border: 2px solid var(--label-edge);
  }
  .label__content {
    position: absolute;
    inset: 0;
    display: flex;
    flex-direction: column;
    align-items: center;
    padding-top: 48px;
  }
  .brand-name {
    font-weight: 300;
    font-size: 44px;
    letter-spacing: 3px;
    line-height: 1;
  }
  .brand-dot {
    width: 54px;
    height: 54px;
    margin-top: 22px;
    border-radius: 50%;
    background: var(--ink-white);
  }
  .tagline {
    margin-top: 24px;
    font-weight: 700;
    font-size: 27px;
    line-height: 1.2;
    word-spacing: 10px;
  }
  .product-type {
    font-weight: 600;
    font-style: italic;
    font-size: 27px;
    line-height: 1.25;
  }
  .volume {
    position: absolute;
    bottom: 26px;
    left: 0;
    right: 0;
    font-weight: 600;
    font-size: 13px;
    letter-spacing: 0.5px;
  }
</style>
</head>
<body>
  <main class="canvas">
    <section class="label">
      <div class="label__frame"></div>
      <div class="label__content">
        <h1 class="brand-name">CLEAR FALL</h1>
        <div class="brand-dot"></div>
        <p class="tagline">So Pure So Fresh</p>
        <p class="product-type">Natural Spring Water</p>
      </div>
      <p class="volume">591ML</p>
    </section>
  </main>
</body>
</html>
```